New Print Material Needed for Renovation Company

We are looking to update our current Print Material to reflect the current process we offer to our clients. A lot of the information is also outdated along with many of the photos that are currently being used. We are a renovation company that specializes in residential and commercial renovations and custom builds.This project is MULTIPLE pages. We will pay the chosen designer an extra fee for the designing 3-4 additional pages that are similar to the chosen design. Attached is our current Print Material. We are hoping to update the look of them and some of the messaging. Our current company colors are white, blue and light grey and it will remain that way.

Industry/Entity Type

Construction Company

Font styles to use
Sans Serif

Colors
3176b5
ffffff

Requirements
Must have
• Easy to explain the process
• Easy to read and understand let alone
• Easy to navigate
Nice to have
• As much creativity as possible
Should not have
• no confusing text
• no confusing layout

```html
<!DOCTYPE html>
<html lang="en">
<head>
<meta charset="utf-8">
<title>Master Builder Timeline – Harbourline General Contractors</title>
<link rel="stylesheet" href="https://fonts.googleapis.com/css2?family=Open+Sans:wght@400;600;700&display=swap">
<style>
  :root {
    --brand-blue: #1254d6;
    --white: #ffffff;
    --ink: #151515;
    --footer-band: #deeaf7;
    --footer-rule: #3e4f5a;
    --box-line: #2a2a2a;
  }
  * { box-sizing: border-box; margin: 0; padding: 0; }
  html, body { width: 1200px; height: 940px; overflow: hidden; background: var(--white); }
  body { position: relative; font-family: "Open Sans", Arial, sans-serif; color: var(--ink); }

  .header-band {
    position: absolute; left: 2px; top: 11px; width: 1191px; height: 220px;
    background: var(--brand-blue);
  }
  .header-badge { position: absolute; left: 30px; top: 65px; width: 112px; height: 112px; }
  .page-title {
    position: absolute; left: 183px; top: 92px;
    font-size: 56px; font-weight: 600; letter-spacing: -1.2px; line-height: 1;
    color: var(--white); white-space: nowrap;
  }
  .company-mark { position: absolute; left: 893px; top: 87px; display: flex; align-items: center; gap: 18px; }
  .company-mark__dot { width: 88px; height: 88px; border: 9px solid var(--white); border-radius: 50%; flex: none; }
  .company-mark__name {
    font-size: 23px; font-weight: 600; line-height: 27px; color: var(--white);
  }

  .stage { position: absolute; top: 261px; width: 400px; height: 520px; }
  .stage--design { left: 20px; }
  .stage--plan   { left: 415px; }
  .stage--build  { left: 831px; }

  .stage__icon { position: absolute; top: 0; width: 160px; height: 150px; }
  .stage--design .stage__icon { left: 98px; }
  .stage--plan   .stage__icon { left: 104px; }
  .stage--build  .stage__icon { left: 96px; }
  .stage__label { font-size: 25px; font-weight: 600; letter-spacing: 1px; fill: var(--brand-blue); }

  .stage__ribbon { position: absolute; left: 1px; top: 160px; width: 35px; height: 341px; }
  .step-number {
    position: absolute; left: 6px; width: 26px; text-align: center;
    font-size: 23px; font-weight: 700; color: var(--white);
  }

  .stage__card {
    position: absolute; left: 44px; top: 151px; width: 299px; height: 361px;
    border: 1px solid var(--box-line); padding: 26px 10px 0 14px;
  }
  .step { height: 121px; }
  .step__title { font-size: 18.5px; font-weight: 600; line-height: 22px; margin-bottom: 6px; white-space: nowrap; }
  .step__text {
    font-size: 11px; font-weight: 600; line-height: 18.3px; letter-spacing: -0.35px;
    text-transform: uppercase; white-space: nowrap;
  }

  .footer-band {
    position: absolute; left: 0; top: 871px; width: 1200px; height: 64px; background: var(--footer-band);
  }
  .footer-rule { position: absolute; left: 0; top: 935px; width: 1200px; height: 5px; background: var(--footer-rule); }
  .footer-tab { position: absolute; left: 713px; top: 882px; width: 477px; height: 43px; }
  .footer-tab__name {
    position: absolute; left: 781px; top: 887px;
    font-size: 23.5px; font-weight: 400; letter-spacing: -0.5px; color: var(--white); white-space: nowrap;
  }
</style>
</head>
<body>

<header class="header-band">
  <svg class="header-badge" viewBox="0 0 112 112" aria-hidden="true">
    <circle cx="56" cy="56" r="52" fill="none" stroke="#fff" stroke-width="3" stroke-dasharray="4 3"/>
    <circle cx="56" cy="56" r="46" fill="none" stroke="#fff" stroke-width="2"/>
    <circle cx="56" cy="56" r="40" fill="none" stroke="#fff" stroke-width="2.5"/>
    <g stroke="#fff" stroke-linecap="round" fill="none">
      <line x1="38" y1="74" x2="66" y2="46" stroke-width="6"/>
      <circle cx="70" cy="42" r="7" stroke-width="5"/>
      <line x1="40" y1="40" x2="72" y2="72" stroke-width="6"/>
    </g>
  </svg>
  <h1 class="page-title">MASTER BUIDER TIMELINE</h1>
  <div class="company-mark">
    <span class="company-mark__dot"></span>
    <span class="company-mark__name">Harbourline<br>General<br>Contractors</span>
  </div>
</header>

<section class="stage stage--design">
  <svg class="stage__icon" viewBox="0 0 160 150">
    <defs><path id="arc-design" d="M 22,102 A 58 58 0 0 1 138,102"/></defs>
    <text class="stage__label"><textPath href="#arc-design" startOffset="50%" text-anchor="middle">DESIGN</textPath></text>
    <circle cx="80" cy="100" r="40" fill="var(--brand-blue)" role="img" aria-label="Icon of two people exchanging ideas"/>
  </svg>
  <svg class="stage__ribbon" viewBox="0 0 35 341" aria-hidden="true"><polygon points="0,0 35,24 35,341 0,314" fill="var(--brand-blue)"/></svg>
  <span class="step-number" style="top:180px">1</span>
  <span class="step-number" style="top:305px">2</span>
  <span class="step-number" style="top:424px">3</span>
  <div class="stage__card">
    <div class="step"><h2 class="step__title">INITIAL DESIGN MEETING</h2><p class="step__text">Lorem ipsum dolor sit amet, consectetur<br>adipiscing elit, sed do eiusmod tempor incidi-<br>dunt ut labore et dolore magna aliqua. Quis</p></div>
    <div class="step"><h2 class="step__title">SECOND DESIGN MEETING</h2><p class="step__text">Lorem ipsum dolor sit amet, consectetur<br>adipiscing elit, sed do eiusmod tempor incidi-<br>dunt ut labore et dolore magna aliqua. Quis</p></div>
    <div class="step"><h2 class="step__title">FINAL DESIGN MEETING</h2><p class="step__text">Lorem ipsum dolor sit amet, consectetur<br>adipiscing elit, sed do eiusmod tempor incidi-<br>dunt ut labore et dolore magna aliqua. Quis</p></div>
  </div>
</section>

<section class="stage stage--plan">
  <svg class="stage__icon" viewBox="0 0 160 150">
    <defs><path id="arc-plan" d="M 24,102 A 56 56 0 0 1 136,102"/></defs>
    <text class="stage__label"><textPath href="#arc-plan" startOffset="50%" text-anchor="middle">PLAN</textPath></text>
    <circle cx="80" cy="100" r="40" fill="var(--brand-blue)"/>
    <circle cx="80" cy="100" r="30" fill="none" stroke="#fff" stroke-width="3"/>
    <g stroke="#fff" stroke-width="3" stroke-linecap="round" stroke-linejoin="round" fill="none">
      <polyline points="62,86 66,90 72,82"/><line x1="77" y1="87" x2="98" y2="87"/>
      <polyline points="62,99 66,103 72,95"/><line x1="77" y1="100" x2="100" y2="100"/>
      <polyline points="62,112 66,116 72,108"/><line x1="77" y1="113" x2="98" y2="113"/>
    </g>
  </svg>
  <svg class="stage__ribbon" viewBox="0 0 35 341" aria-hidden="true"><polygon points="0,0 35,24 35,341 0,314" fill="var(--brand-blue)"/></svg>
  <span class="step-number" style="top:196px">1</span>
  <span class="step-number" style="top:305px">2</span>
  <span class="step-number" style="top:424px">3</span>
  <div class="stage__card">
    <div class="step"><h2 class="step__title">INITIAL DESIGN MEETING</h2><p class="step__text">Lorem ipsum dolor sit amet, consectetur<br>adipiscing elit, sed do eiusmod tempor incidi-<br>dunt ut labore et dolore magna aliqua. Quis</p></div>
    <div class="step"><h2 class="step__title">SECOND DESIGN MEETING</h2><p class="step__text">Lorem ipsum dolor sit amet, consectetur<br>adipiscing elit, sed do eiusmod tempor incidi-<br>dunt ut labore et dolore magna aliqua. Quis</p></div>
    <div class="step"><h2 class="step__title">FINAL DESIGN MEETING</h2><p class="step__text">Lorem ipsum dolor sit amet, consectetur<br>adipiscing elit, sed do eiusmod tempor incidi-<br>dunt ut labore et dolore magna aliqua. Quis</p></div>
  </div>
</section>

<section class="stage stage--build">
  <svg class="stage__icon" viewBox="0 0 160 150">
    <defs><path id="arc-build" d="M 24,102 A 56 56 0 0 1 136,102"/></defs>
    <text class="stage__label"><textPath href="#arc-build" startOffset="50%" text-anchor="middle">BUILD</textPath></text>
    <circle cx="80" cy="100" r="40" fill="var(--brand-blue)"/>
    <circle cx="80" cy="100" r="30" fill="none" stroke="#fff" stroke-width="3"/>
    <g fill="#fff">
      <rect x="63" y="108" width="5" height="10"/><rect x="70" y="105" width="5" height="13"/>
      <rect x="77" y="102" width="5" height="16"/><rect x="84" y="98" width="5" height="20"/>
      <rect x="91" y="93" width="5" height="25"/>
      <polygon points="88,76 100,80 95,83"/>
    </g>
    <path d="M 62,102 Q 82,98 95,81" fill="none" stroke="#fff" stroke-width="4" stroke-linecap="round"/>
  </svg>
  <svg class="stage__ribbon" viewBox="0 0 35 341" aria-hidden="true"><polygon points="0,0 35,24 35,341 0,314" fill="var(--brand-blue)"/></svg>
  <span class="step-number" style="top:189px">1</span>
  <span class="step-number" style="top:307px">2</span>
  <span class="step-number" style="top:421px">3</span>
  <div class="stage__card">
    <div class="step"><h2 class="step__title">INITIAL DESIGN MEETING</h2><p class="step__text">Lorem ipsum dolor sit amet, consectetur<br>adipiscing elit, sed do eiusmod tempor incidi-<br>dunt ut labore et dolore magna aliqua. Quis</p></div>
    <div class="step"><h2 class="step__title">SECOND DESIGN MEETING</h2><p class="step__text">Lorem ipsum dolor sit amet, consectetur<br>adipiscing elit, sed do eiusmod tempor incidi-<br>dunt ut labore et dolore magna aliqua. Quis</p></div>
    <div class="step"><h2 class="step__title">FINAL DESIGN MEETING</h2><p class="step__text">Lorem ipsum dolor sit amet, consectetur<br>adipiscing elit, sed do eiusmod tempor incidi-<br>dunt ut labore et dolore magna aliqua. Quis</p></div>
  </div>
</section>

<footer>
  <div class="footer-band"></div>
  <div class="footer-rule"></div>
  <svg class="footer-tab" viewBox="0 0 477 43" aria-hidden="true"><polygon points="0,0 417,0 477,43 51,43" fill="var(--brand-blue)"/></svg>
  <span class="footer-tab__name">Harbourline General Contractors</span>
</footer>

</body>
</html>
```